Post storm repair flyer

looking for an eye catching 6x9 postcard to send out to single family home owners advertising a "Post Storm Repair Special" explaining that after the recent hurricanes its very important to have your roof checked and any repairs fixed right away before they become a bigger more costly problem and that even though your home wasn't directly hit by the storm the high wind gust could've cause unseen damage.
offer $200 off any repair *some rules may apply
Lark Roofing
888.417.LARK
www.LarkRoofing.example

Roofing

```html
<!DOCTYPE html>
<html lang="en">
<head>
<meta charset="utf-8">
<title>Lark Roofing – Post Storm Repair Special Postcard</title>
<link rel="stylesheet" href="https://fonts.googleapis.com/css2?family=Oswald:wght@400;500;600;700&display=swap">
<style>
  :root {
    --backdrop: #787878;
    --amber: #f4a711;
    --ink: #0b0b0d;
    --night-a: #0c0e13;
    --night-b: #20232b;
    --slate: #45464b;
    --paper: #ffffff;
    --rule: #a9a9a9;
    --stamp: #b3b3b3;
  }
  * { margin: 0; padding: 0; box-sizing: border-box; }
  html, body { width: 1200px; height: 2539px; overflow: hidden; }
  body {
    background: var(--backdrop);
    font-family: "Oswald", sans-serif;
    position: relative;
  }
  .postcard {
    position: absolute;
    left: 168px;
    width: 864px;
    height: 574px;
    display: block;
    box-shadow: 0 12px 30px rgba(0,0,0,.25);
  }
  .postcard--front { top: 660px; }
  .postcard--back { top: 1305px; }

  .fill-amber { fill: var(--amber); }
  .fill-ink { fill: var(--ink); }
  .fill-paper { fill: var(--paper); }
  .fill-stamp { fill: var(--stamp); }
  .frame { fill: url(#photoTone); stroke: var(--amber); stroke-width: 8; stroke-linejoin: round; }
  .photo-box { fill: url(#photoTone); stroke: var(--amber); stroke-width: 5; }
  .address-rule { stroke: var(--rule); stroke-width: 2.5; }

  .wordmark { font-family: "Oswald", sans-serif; font-weight: 400; fill: var(--ink); letter-spacing: .5px; }
  .headline { font-family: "Oswald", sans-serif; font-weight: 700; }
  .headline--white { fill: var(--paper); }
  .headline--amber { fill: var(--amber); }
  .offer { font-family: "Oswald", sans-serif; font-weight: 500; font-size: 42px; }
  .offer-amber { fill: var(--amber); }
  .offer-white { fill: var(--paper); }
  .fine-print { font-family: "Oswald", sans-serif; font-weight: 400; font-size: 23px; fill: var(--paper); }
  .phone { font-family: "Oswald", sans-serif; font-weight: 500; font-size: 40px; fill: var(--paper); }
  .url { font-family: "Oswald", sans-serif; font-weight: 500; font-size: 28px; fill: var(--ink); }
  .section-title { font-family: "Oswald", sans-serif; font-weight: 400; font-size: 30px; fill: var(--paper); }
  .caption { font-family: "Oswald", sans-serif; font-weight: 400; font-size: 14px; fill: var(--paper); text-anchor: middle; }
  .icon-line { fill: none; stroke: var(--paper); stroke-width: 3; stroke-linecap: round; }
</style>
</head>
<body>

<svg width="0" height="0" style="position:absolute" aria-hidden="true">
  <defs>
    <linearGradient id="photoTone" x1="0" y1="0" x2="1" y2="1">
      <stop offset="0" stop-color="#8c95a3"/>
      <stop offset="1" stop-color="#4f5866"/>
    </linearGradient>
    <linearGradient id="nightTone" x1="0" y1="0" x2="1" y2="0">
      <stop offset="0" stop-color="#0c0e13"/>
      <stop offset="1" stop-color="#22252d"/>
    </linearGradient>
    <linearGradient id="slateTone" x1="0" y1="0" x2="0" y2="1">
      <stop offset="0" stop-color="#3e3f44"/>
      <stop offset="1" stop-color="#4a4b50"/>
    </linearGradient>
    <symbol id="phoneIcon" viewBox="0 0 40 40">
      <path d="M10 6 L16 6 L18 14 L14 17 Q17 24 23 27 L26 23 L34 25 L34 31 Q30 36 24 34 Q10 29 6 16 Q5 9 10 6 Z" fill="#ffffff"/>
      <path class="icon-line" d="M22 8 Q31 10 33 19"/>
      <path class="icon-line" d="M21 14 Q26 15 27 20"/>
    </symbol>
    <symbol id="mailIcon" viewBox="0 0 34 24">
      <rect x="1" y="1" width="32" height="22" fill="#0b0b0d"/>
      <path d="M2 2 L17 14 L32 2" fill="none" stroke="#f4a711" stroke-width="2.5"/>
      <path d="M2 22 L13 11 M32 22 L21 11" fill="none" stroke="#f4a711" stroke-width="2"/>
    </symbol>
  </defs>
</svg>

<!-- Front -->
<svg class="postcard postcard--front" viewBox="0 0 864 574" role="group" aria-label="Postcard front">
  <rect class="fill-paper" width="864" height="113"/>
  <rect y="113" width="864" height="380" fill="url(#nightTone)"/>

  <g class="brand">
    <rect class="fill-ink" x="74" y="40" width="26" height="26"/>
    <text class="wordmark" x="54" y="100" font-size="15">LARKROOFING.EXAMPLE</text>
  </g>

  <polygon class="frame" points="569,18 723,107 723,285 569,374 415,285 415,107" role="img" aria-label="Close-up photo of grey asphalt roof shingles"/>
  <polygon class="frame" points="384,221 446,257 446,329 384,365 322,329 322,257" role="img" aria-label="Photo of a shingled roof ridge"/>
  <polygon class="frame" points="754,221 816,257 816,329 754,365 692,329 692,257" role="img" aria-label="Photo of a shingled roof under a bright sky"/>

  <g class="headline-block">
    <text class="headline headline--amber" x="48" y="175" font-size="52" font-weight="500">Post</text>
    <text class="headline headline--white" x="46" y="238" font-size="68">STORM</text>
    <text class="headline headline--white" x="46" y="301" font-size="68">REPAIR</text>
    <text class="headline headline--amber" x="46" y="364" font-size="68">SPECIAL</text>
    <text class="offer" x="46" y="425"><tspan class="offer-amber">Offer </tspan><tspan class="offer-white">$200</tspan><tspan class="offer-amber"> off any repair</tspan></text>
    <text class="fine-print" x="48" y="455">*some rules may apply</text>
  </g>

  <g class="contact-bar">
    <rect class="fill-amber" y="483" width="864" height="91"/>
    <polygon class="fill-ink" points="0,493 382,493 462,574 0,574"/>
    <rect class="fill-ink" x="462" y="566" width="402" height="8"/>
    <use href="#phoneIcon" x="46" y="518" width="36" height="36"/>
    <text class="phone" x="96" y="551">888.417.LARK</text>
    <use href="#mailIcon" x="505" y="532" width="32" height="22"/>
    <text class="url" x="550" y="553" textLength="268" lengthAdjust="spacingAndGlyphs">www.LarkRoofing.example</text>
  </g>

  <polygon class="frame" points="569,381 631,417 631,489 569,525 507,489 507,417" role="img" aria-label="Photo of a house gable with siding"/>
</svg>

<!-- Back -->
<svg class="postcard postcard--back" viewBox="0 0 864 574" role="group" aria-label="Postcard back">
  <rect class="fill-paper" width="864" height="574"/>
  <rect width="462" height="482" fill="url(#slateTone)"/>

  <text class="section-title" x="48" y="50">Our Services</text>

  <g class="service-grid">
    <rect class="photo-box" x="50" y="76" width="170" height="150" role="img" aria-label="Photo of a house gable roof"/>
    <text class="caption" x="135" y="246">Retail/Commercial</text>
    <text class="caption" x="135" y="262">Roof Replacement</text>

    <rect class="photo-box" x="245" y="76" width="170" height="150" role="img" aria-label="Photo of storm damaged roof shingles"/>
    <text class="caption" x="330" y="246">Storm Damage</text>
    <text class="caption" x="330" y="262">Roof Replacement</text>

    <rect class="photo-box" x="50" y="278" width="170" height="150" role="img" aria-label="Photo of a house under construction"/>
    <text class="caption" x="135" y="452">New Construction</text>

    <rect class="photo-box" x="245" y="278" width="170" height="150" role="img" aria-label="Photo of a roof covered with a blue tarp"/>
    <text class="caption" x="330" y="452">Repairs &amp; Restoration</text>
  </g>

  <g class="mailing-side">
    <rect class="fill-ink" x="606" y="42" width="20" height="20"/>
    <text class="wordmark" x="616" y="92" font-size="10" text-anchor="middle">LARKROOFING.EXAMPLE</text>
    <rect class="fill-stamp" x="734" y="34" width="80" height="71"/>
    <line class="address-rule" x1="502" y1="184" x2="815" y2="184"/>
    <line class="address-rule" x1="502" y1="229" x2="815" y2="229"/>
    <line class="address-rule" x1="502" y1="275" x2="815" y2="275"/>
  </g>

  <g class="contact-bar">
    <rect class="fill-amber" y="482" width="864" height="92"/>
    <polygon class="fill-ink" points="0,492 382,492 462,574 0,574"/>
    <rect class="fill-ink" x="462" y="566" width="402" height="8"/>
    <use href="#phoneIcon" x="46" y="518" width="36" height="36"/>
    <text class="phone" x="96" y="551">888.417.LARK</text>
    <use href="#mailIcon" x="505" y="515" width="32" height="22"/>
    <text class="url" x="550" y="536" textLength="268" lengthAdjust="spacingAndGlyphs">www.LarkRoofing.example</text>
  </g>
</svg>

</body>
</html>
```